Wine label design for my wife. Wine called "The Mirabel"

I need a wine label face lift of one of my premium wines in my collection. My wine sells in Harbor Lark's all over the States. My current label is called The Mirabel (my wife's name) and the illustration of her eyes is done by a well know artist from South Africa. I do not have to use this illustration and therefor I attached several pictures of her and her eyes, even when she was a little girl. The wine's also made in South Africa. This is a premium wine that we only sell 2000 bottles per year. The wine sells at 60 usd per bottle, The current label is too white. I also think her eyes should look more at the person buying it, than away from them.

Target Market(s)

Top end wine buyers

Font styles to use
Decorative
Script

Requirements
Must have
• 'The Mirabel' must be on the label
An illustration must be on the label
Basically all the info that's on the current label must be on by law. As per Sample
Nice to have
• Maybe some ideas of her whole face?
Should not have
• any gold colour

```html
<!DOCTYPE html>
<html lang="en">
<head>
<meta charset="utf-8">
<title>The Mirabel – Sauvignon Blanc Label</title>
<link href="https://fonts.googleapis.com/css2?family=Allura&family=Exo+2:wght@300;400&family=Libre+Baskerville&display=swap" rel="stylesheet">
<style>
  :root {
    --page-bg: #ffffff;
    --label-top-dark: #19191a;
    --label-top-light: #434346;
    --label-bottom-light: #3c3c3f;
    --label-bottom-dark: #1d1d1e;
    --band-edge: #0f0f0f;
    --band-shade: #262626;
    --band-light: #4a4a4a;
    --ink-white: #ffffff;
    --ink-muted: #6f6f72;
    --ink-soft: #8a8a8d;
  }
  * { margin: 0; padding: 0; box-sizing: border-box; }
  html, body {
    width: 1200px;
    height: 927px;
    overflow: hidden;
    background: var(--page-bg);
  }
  .canvas {
    position: relative;
    width: 1200px;
    height: 927px;
  }
  .wine-label {
    position: absolute;
    left: 444px;
    top: 260px;
    width: 313px;
    height: 407px;
    overflow: hidden;
    background: var(--label-bottom-dark);
  }
  .label-head {
    position: absolute;
    left: 0; top: 0;
    width: 100%;
    height: 150px;
    background: linear-gradient(to bottom, var(--label-top-dark), var(--label-top-light));
  }
  .label-foot {
    position: absolute;
    left: 0; top: 272px;
    width: 100%;
    height: 135px;
    background: linear-gradient(to bottom, var(--label-bottom-light), var(--label-bottom-dark));
  }
  .wine-name {
    position: absolute;
    left: 0; top: 0;
    width: 100%;
    height: 110px;
    color: var(--ink-white);
    font-weight: normal;
  }
  .wine-name__article {
    position: absolute;
    left: 126px;
    top: 40px;
    font-family: "Exo 2", sans-serif;
    font-weight: 300;
    font-size: 13px;
    line-height: 14px;
    letter-spacing: 0.5px;
  }
  .wine-name__title {
    position: absolute;
    left: 0;
    top: 50px;
    width: 100%;
    text-align: center;
    font-family: "Allura", cursive;
    font-size: 60px;
    line-height: 60px;
    padding-left: 4px;
  }
  .wine-name__swash {
    position: absolute;
    left: 113px;
    top: 104px;
  }
  .portrait-band {
    position: absolute;
    left: 0; top: 148px;
    width: 100%;
    height: 126px;
    background:
      radial-gradient(ellipse 38% 30% at 30% 50%, rgba(90,90,90,0.55), transparent 70%),
      radial-gradient(ellipse 38% 30% at 70% 50%, rgba(90,90,90,0.55), transparent 70%),
      linear-gradient(to right, var(--band-edge) 0%, var(--band-shade) 12%, var(--band-light) 50%, var(--band-shade) 88%, var(--band-edge) 100%);
  }
  .torn-edge {
    position: absolute;
    left: 0;
    width: 100%;
    height: 12px;
  }
  .torn-edge--top { top: 141px; }
  .torn-edge--bottom { top: 267px; }
  .wine-details {
    position: absolute;
    left: 0; top: 296px;
    width: 100%;
    text-align: center;
    color: var(--ink-white);
  }
  .wine-details__variety {
    font-family: "Exo 2", sans-serif;
    font-weight: 300;
    font-size: 15px;
    letter-spacing: 0.6px;
    line-height: 18px;
  }
  .wine-details__vintage {
    margin-top: 16px;
    font-family: "Exo 2", sans-serif;
    font-weight: 400;
    font-size: 15px;
    line-height: 18px;
  }
  .wine-details__producer {
    margin-top: 14px;
    font-family: "Libre Baskerville", serif;
    font-size: 10.5px;
    letter-spacing: 2.8px;
    color: var(--ink-muted);
    line-height: 13px;
  }
  .wine-details__origin {
    margin-top: 4px;
    font-family: "Exo 2", sans-serif;
    font-weight: 300;
    font-size: 10px;
    letter-spacing: 0.5px;
    color: var(--ink-soft);
  }
</style>
</head>
<body>
<main class="canvas">
  <section class="wine-label">
    <div class="label-head"></div>

    <h1 class="wine-name">
      <span class="wine-name__title">Mirabel</span>
      <span class="wine-name__article">The</span>
    </h1>
    <svg class="wine-name__swash" width="90" height="14" viewBox="0 0 90 14" aria-hidden="true">
      <path d="M2 9 C 25 3, 55 1, 86 8" stroke="#ffffff" stroke-width="1.8" fill="none" stroke-linecap="round"/>
    </svg>

    <div class="portrait-band" role="img" aria-label="Black-and-white illustration of Mirabel's eyes looking at the viewer, cropped to a narrow horizontal strip"></div>

    <svg class="torn-edge torn-edge--top" viewBox="0 0 313 12" preserveAspectRatio="none" aria-hidden="true">
      <polygon fill="#ffffff" points="0,3 20,2 45,4 70,2 95,3 120,1 150,3 175,2 200,4 230,2 255,3 285,1 313,3 313,9 290,8 260,10 235,8 205,9 180,7 150,9 120,8 95,10 65,8 40,9 15,7 0,9"/>
    </svg>
    <svg class="torn-edge torn-edge--bottom" viewBox="0 0 313 12" preserveAspectRatio="none" aria-hidden="true">
      <polygon fill="#ffffff" points="0,4 25,3 50,2 80,4 105,2 135,3 160,1 190,3 215,2 245,4 270,2 295,3 313,2 313,9 285,10 260,8 230,9 200,10 170,8 140,9 110,8 85,10 55,9 30,10 0,10"/>
    </svg>

    <div class="label-foot"></div>

    <div class="wine-details">
      <p class="wine-details__variety">Savignon Blanc</p>
      <p class="wine-details__vintage">2017</p>
      <p class="wine-details__producer">DANIEL REED WINES</p>
      <p class="wine-details__origin">South Africa</p>
    </div>
  </section>
</main>
</body>
</html>
```